Modern Yoga Studio Timetable and Flyer Design

We have a comprehensive class timetable and we are wanting to a clean modern look for our Spring timetable.

We require a double sided flyer with our class timetable included.
We would prefer an A5 size (postcard) or DL (1/3 A4).

We would like the final flyer to have.
Side A : Yoga image, logo

Fennel Stretch Hall
address: 4/71 Wexcombe Lane, Pelharton
website: fennelstretch.com.au
mobile: 0471 296 814

Side B: Clear easy to read timetable with a break down of class types and website.

We would also like to have a copy of the timetable itself as a separate jpg or pdf for use on our website to download.

Thank you.
Yours kindly,
Nell

I have attached a sample of another timetable of which I like the look and feel of, however this is just a guide. I've also attached our 'new' schedule in WORD plus uploaded our last design of the front.
Updates

Target Market(s)

Women aged 30-45

Industry/Entity Type

Health And Wellness

Font styles to use
Other font styles liked:
• Brandon Grotesque, Jenna Sue

Colors
6c459b
33a6d7
ffffff

Requirements
Must have
• A definitive colour to decipher between different class types on our timetable. Where each colour represents a different class type. Colours and layouts similar to our website design, see www.fennelstretch.com.au
Nice to have
• I've included a design of another studio whose timetable design I like. One of our own yoga images instead of a stock image.
Should not have
• No dark gridlines between the cells/boxes in the timetables. Please don't use stock yoga images.

```html
<!DOCTYPE html>
<html lang="en">
<head>
<meta charset="utf-8">
<title>Fennel Stretch Hall – Spring Flyer</title>
<link href="https://fonts.googleapis.com/css2?family=Josefin+Sans:wght@300;400;600;700&family=Caveat:wght@400;500&display=swap" rel="stylesheet">
<style>
  :root{
    --navy:#1c1f4f;
    --purple:#6c459b;
    --sky:#33a6d7;
    --white:#ffffff;
    --page:#efefef;
    --ink:#1c1f4f;
    --gridline:#e9eff4;
    --sand:#b99468;
    --c-rise:#f4d81f;
    --c-vinyasa:#86cfbd;
    --c-slow:#2b8fcf;
    --c-yin:#dcdcdc;
    --c-pregnancy:#f29a9e;
    --c-mumbaby:#c8278f;
    --c-kids-older:#9cc45a;
    --c-kids-young:#a9a5d8;
    --c-teens:#6cc07a;
    --c-flow-restore:#efe94a;
    --c-yin-restore:#93a8a7;
    --c-womens:#f7a21b;
  }
  *{box-sizing:border-box;margin:0;padding:0}
  html,body{width:1200px;height:1200px;overflow:hidden;background:var(--page)}
  body{position:relative;font-family:"Josefin Sans",Arial,sans-serif;color:var(--ink)}

  /* Front side */
  .flyer-front{position:absolute;left:73px;top:62px;width:1064px;height:508px;background:var(--navy);padding:7px 7px 0}
  .front-art{position:relative;width:1050px;height:443px;background:var(--white);overflow:hidden}
  .floor{position:absolute;left:0;right:0;bottom:0;height:100px;background:linear-gradient(180deg,#c7a477,var(--sand))}
  .ornament{position:absolute;left:240px;top:-7px;width:496px;height:178px;border-radius:0 0 248px 248px;background:radial-gradient(ellipse at 50% 0,rgba(108,69,155,.55),rgba(108,69,155,.18) 55%,rgba(200,200,210,.25) 80%,rgba(255,255,255,0) 100%)}
  .photo{position:absolute;background:linear-gradient(160deg,#d8b89a,#8a4fa8 40%,#e2a06a 70%,#efe7df)}
  .photo-left{left:12px;top:91px;width:452px;height:352px;clip-path:polygon(10% 0,45% 5%,70% 50%,100% 100%,0 100%,20% 60%)}
  .photo-right{left:560px;top:119px;width:488px;height:324px;clip-path:polygon(40% 0,70% 20%,95% 85%,100% 100%,0 100%,30% 40%)}
  .brand{position:absolute;left:0;right:0;top:120px;text-align:center}
  .brand-name{font-family:"Josefin Sans",Arial,sans-serif;font-weight:400;font-size:40px;letter-spacing:6px;color:var(--sky);background:rgba(255,255,255,.8);padding:4px 14px}
  .tagline{position:absolute;left:0;right:0;text-align:center;font-family:"Caveat",cursive;color:var(--ink)}
  .tag-1{top:196px;font-size:30px}
  .tag-2{top:230px;font-size:44px;color:var(--sky)}
  .tag-3{top:282px;font-size:30px}
  .front-contact{display:flex;align-items:center;justify-content:center;height:58px;color:var(--white);font-size:21px}
  .front-contact span{padding:0 40px}
  .front-contact b{font-weight:700}
  .divider{width:1px;height:26px;background:var(--white);padding:0!important}

  /* Timetable side */
  .flyer-back{position:absolute;left:73px;top:619px;width:1064px;height:509px;background:var(--white)}
  .back-header{height:43px;background:var(--navy);color:var(--white);display:flex;align-items:center;justify-content:center;font-weight:700;font-size:20px;letter-spacing:6px}
  .back-header .dots{letter-spacing:2px;font-size:14px;margin:0 8px}
  .timetable{position:absolute;left:45px;top:43px;width:976px;display:grid;grid-template-columns:repeat(8,122px);grid-template-rows:32px repeat(13,31px);
    background-image:linear-gradient(90deg,var(--gridline) 1px,transparent 1px),linear-gradient(180deg,var(--gridline) 1px,transparent 1px);
    background-size:122px 100%,100% 31px;background-position:0 0,0 32px}
  .day{grid-row:1;display:flex;align-items:flex-end;justify-content:center;font-size:21px;font-weight:400;padding-bottom:2px}
  .time{grid-column:1;display:flex;align-items:center;padding-left:24px;font-size:18px}
  .time small{font-size:14px}
  .class{margin:3px 3px 2px;display:flex;align-items:center;justify-content:center;font-size:15px;font-weight:300;text-transform:uppercase;white-space:nowrap;color:var(--ink)}
  .light{color:var(--white)}
  .rise{background:var(--c-rise)}
  .vinyasa{background:var(--c-vinyasa)}
  .slow{background:var(--c-slow)}
  .yin{background:var(--c-yin)}
  .pregnancy{background:var(--c-pregnancy)}
  .mumbaby{background:var(--c-mumbaby)}
  .kids-older{background:var(--c-kids-older)}
  .kids-young{background:var(--c-kids-young)}
  .teens{background:var(--c-teens)}
  .flow-restore{background:var(--c-flow-restore);letter-spacing:-.5px}
  .yin-restore{background:var(--c-yin-restore)}
  .womens{background:var(--c-womens);font-size:11px;letter-spacing:-.4px}
  .footnote{position:absolute;left:70px;top:486px;font-size:9px}
</style>
</head>
<body>

<section class="flyer-front">
  <div class="front-art">
    <div class="ornament" role="img" aria-label="Decorative purple mandala pattern"></div>
    <div class="floor" role="img" aria-label="Woven sisal floor mat"></div>
    <div class="photo photo-left" role="img" aria-label="Photo of a yoga teacher in a twisted side-angle pose"></div>
    <div class="photo photo-right" role="img" aria-label="Photo of a yoga teacher in downward-facing dog"></div>
    <div class="brand"><span class="brand-name">Fennel Stretch Hall</span></div>
    <p class="tagline tag-1">Inclusive, Inspiring Boutique</p>
    <p class="tagline tag-2">Yoga Studio Classes</p>
    <p class="tagline tag-3">for all ages + Abilities</p>
  </div>
  <div class="front-contact">
    <span>4/71 Wexcombe Lane, Pelharton</span>
    <span class="divider"></span>
    <span>website: <b>fennelstretch.com.au</b></span>
    <span class="divider"></span>
    <span>mobile: <b>0471 296 814</b></span>
  </div>
</section>

<section class="flyer-back">
  <h1 class="back-header"><span class="dots">•••••</span>FENNEL STRETCH SPRING TIMETABLE<span class="dots">•••••</span></h1>
  <div class="timetable">
    <div class="day" style="grid-column:2">MON</div>
    <div class="day" style="grid-column:3">TUE</div>
    <div class="day" style="grid-column:4">WED</div>
    <div class="day" style="grid-column:5">THU</div>
    <div class="day" style="grid-column:6">FRI</div>
    <div class="day" style="grid-column:7">SAT</div>
    <div class="day" style="grid-column:8">SUN</div>

    <div class="time" style="grid-row:2">5:45<small>AM</small></div>
    <div class="time" style="grid-row:3">9:00<small>AM</small></div>
    <div class="time" style="grid-row:4">9:15<small>AM</small></div>
    <div class="time" style="grid-row:5">9:30<small>AM</small></div>
    <div class="time" style="grid-row:6">10:30<small>AM</small></div>
    <div class="time" style="grid-row:7">11:00<small>AM</small></div>
    <div class="time" style="grid-row:8">12:15<small>PM</small></div>
    <div class="time" style="grid-row:9">4:00<small>PM</small></div>
    <div class="time" style="grid-row:10">4:45<small>PM</small></div>
    <div class="time" style="grid-row:11">5:00<small>PM</small></div>
    <div class="time" style="grid-row:12">6:00<small>PM</small></div>
    <div class="time" style="grid-row:13">6:15<small>PM</small></div>
    <div class="time" style="grid-row:14">7:30<small>PM</small></div>

    <div class="class rise" style="grid-area:2/3">RISE + SHINE*</div>
    <div class="class rise" style="grid-area:2/5">RISE + SHINE*</div>
    <div class="class vinyasa" style="grid-area:3/7">VINYASA FLOW</div>
    <div class="class vinyasa" style="grid-area:4/3">VINYASA FLOW</div>
    <div class="class yin" style="grid-area:4/8">YIN</div>
    <div class="class slow light" style="grid-area:5/2">SLOW FLOW</div>
    <div class="class vinyasa" style="grid-area:5/5">VINYASA FLOW</div>
    <div class="class pregnancy" style="grid-area:6/7">PREGNANCY*</div>
    <div class="class mumbaby light" style="grid-area:7/3">MUM + BABY*</div>
    <div class="class mumbaby light" style="grid-area:7/5">MUM + BABY*</div>
    <div class="class pregnancy" style="grid-area:8/5">PREGNANCY</div>
    <div class="class kids-older" style="grid-area:9/4">KIDS 8-12*</div>
    <div class="class kids-young" style="grid-area:9/5">KIDS 5- 7*</div>
    <div class="class vinyasa" style="grid-area:9/7">VINYASA FLOW</div>
    <div class="class teens" style="grid-area:10/4">TEENS 12-16*</div>
    <div class="class teens" style="grid-area:11/5">TEENS 12-16*</div>
    <div class="class pregnancy" style="grid-area:12/2">PREGNANCY*</div>
    <div class="class vinyasa" style="grid-area:12/3">VINYASA FLOW</div>
    <div class="class slow light" style="grid-area:12/4">SLOW FLOW</div>
    <div class="class flow-restore" style="grid-area:12/6">FLOW + RESTORE</div>
    <div class="class pregnancy" style="grid-area:13/5">PREGNANCY*</div>
    <div class="class vinyasa" style="grid-area:14/2">VINYASA FLOW</div>
    <div class="class pregnancy" style="grid-area:14/3">PREGNANCY*</div>
    <div class="class yin-restore" style="grid-area:14/4">YIN + RESTORE</div>
    <div class="class womens" style="grid-area:14/5">WOMEN'S WELLNESS*</div>
  </div>
  <p class="footnote">* bookings essential</p>
</section>

</body>
</html>
```